Orvex App Form Input Screens - Sleek Clean Design

We have a input form that we would like to transpose into an Orvex App. We have a programmer to do the screens but we need to take this very field heavy form and get it into clean design input screens (We can as many screens as make sense). We want to design to be slick and intuitive. This will be used by young guys who enjoy a gaming atmosphere. But the design has to be easy enough to be completely intuitive to a novice user. The Company likes to do things with Sky Blue colors. Also OK to incorporate burnt orange/yellow (Think glowing sun).

Target Market(s)

18-25 year old males - These guys go door to door and input this data all day

Industry/Entity Type

Solar Energy

Number of Pages Required

5+ page

Font styles to use
Sans Serif

Colors
0355a3
3277b5
85acd3
d0dfed
faa54b
ffc214
f68e4d

Requirements
Must have
• Clean simple sleek Designs - Drop Down Examples. The background and fields have to have distinct colors because these guys will be outside most of the time and if the design is not contrasted enough, it will be hard for them to see.
Nice to have
• Fun ways to incorporate the Glowing Sun Colors (Subtle)
Should not have
• Should not look like Powerpoint

```html
<!DOCTYPE html>
<html lang="en">
<head>
<meta charset="utf-8">
<title>Solar Energy – Customer Information</title>
<link href="https://fonts.googleapis.com/css2?family=Roboto:wght@300;400;500&display=swap" rel="stylesheet">
<style>
  :root{
    --sky-deep:#0355a3;
    --sky:#3277b5;
    --sky-soft:#85acd3;
    --sky-mist:#d0dfed;
    --sun:#faa54b;
    --sun-bright:#ffc214;
    --sun-burnt:#f68e4d;
    --page:#eef0f3;
    --field:#ffffff;
    --field-line:#c9ced6;
    --label:#5d6670;
    --ink:#4a525b;
    --canvas:#e4e8ee;
  }
  *{box-sizing:border-box;margin:0;padding:0}
  html,body{width:1200px;height:1200px;overflow:hidden}
  body{background:var(--canvas);font-family:"Roboto",sans-serif;color:var(--ink)}
  .screen{position:absolute;left:40px;top:180px;width:1120px;height:840px;background:var(--page);overflow:hidden;box-shadow:0 10px 40px rgba(3,85,163,.18)}
  .status-bar{position:absolute;left:0;top:0;width:100%;height:28px;background:var(--sky);color:#fff;font-size:13px;display:flex;align-items:center;justify-content:space-between;padding:0 14px}
  .status-bar .carrier,.status-bar .power{display:flex;align-items:center;gap:6px}
  .status-bar .time{position:absolute;left:50%;transform:translateX(-50%);font-weight:500}
  .app-header{position:absolute;left:0;top:28px;width:100%;height:82px;background:var(--sky);display:flex;align-items:center;justify-content:center}
  .app-title{color:#fff;font-size:30px;font-weight:400;letter-spacing:.2px}
  .stepper{position:absolute;left:0;top:110px;width:100%;height:66px;background:var(--sky-mist)}
  .stepper svg{position:absolute;left:0;top:0}
  .form-title{position:absolute;left:0;top:192px;width:100%;text-align:center;font-size:36px;font-weight:300;color:var(--ink)}
  .field{position:absolute}
  .field label{display:block;font-size:16px;color:var(--label);margin-bottom:8px}
  .field .box{height:56px;background:var(--field);border:1px solid var(--field-line);display:flex;align-items:center;padding:0 16px;font-size:16px;color:var(--label)}
  .field .select{padding-right:0;justify-content:space-between}
  .select .chevron{width:56px;height:56px;margin:-1px -1px -1px 0;background:var(--sky);display:flex;align-items:center;justify-content:center}
  .footer-band{position:absolute;left:0;bottom:0;width:100%;height:110px;background:linear-gradient(90deg,var(--sky) 0%,#4a8cc7 60%,var(--sky-soft) 88%,var(--sky) 100%)}
  .btn{position:absolute;top:30px;height:52px;border-radius:26px;font-family:"Roboto",sans-serif;font-size:19px;display:flex;align-items:center;justify-content:center;border:none}
  .btn-previous{left:560px;width:136px;background:#fff;color:#8a929b}
  .btn-next{left:716px;width:136px;background:var(--sun);color:#fff;font-weight:500;box-shadow:0 0 18px rgba(255,194,20,.45)}
</style>
</head>
<body>
  <main class="screen">
    <div class="status-bar">
      <div class="carrier">
        <svg width="46" height="8" viewBox="0 0 46 8"><g fill="#fff"><circle cx="4" cy="4" r="3.3"/><circle cx="13" cy="4" r="3.3"/><circle cx="22" cy="4" r="3.3"/></g><g fill="none" stroke="#fff" stroke-width="1"><circle cx="31" cy="4" r="3"/><circle cx="40" cy="4" r="3"/></g></svg>
        <span>NOVA</span>
        <svg width="15" height="11" viewBox="0 0 15 11"><path d="M1 4a9 9 0 0 1 13 0M3.5 6.5a5.5 5.5 0 0 1 8 0" fill="none" stroke="#fff" stroke-width="1.6" stroke-linecap="round"/><circle cx="7.5" cy="9.3" r="1.4" fill="#fff"/></svg>
      </div>
      <span class="time">4:21 PM</span>
      <div class="power">
        <svg width="8" height="12" viewBox="0 0 8 12"><path d="M1 3.5l6 5-3 2.5V1l3 2.5-6 5" fill="none" stroke="#fff" stroke-width="1.1"/></svg>
        <span>22%</span>
        <svg width="26" height="12" viewBox="0 0 26 12"><rect x=".5" y=".5" width="22" height="11" rx="2" fill="none" stroke="#fff"/><rect x="2" y="2" width="5" height="8" fill="#fff"/><rect x="23.5" y="4" width="2" height="4" fill="#fff"/></svg>
      </div>
    </div>

    <header class="app-header"><h1 class="app-title">Solar Energy</h1></header>

    <nav class="stepper" aria-label="Form progress, step 2 of 9">
      <svg width="1120" height="66" viewBox="0 0 1120 66" font-family="Roboto, sans-serif" font-size="13" text-anchor="middle">
        <line x1="110" y1="33" x2="1023" y2="33" stroke="#fff" stroke-width="2"/>
        <line x1="110" y1="33" x2="224" y2="33" stroke="var(--sky)" stroke-width="3"/>
        <g>
          <circle cx="110" cy="33" r="15" fill="var(--sky)"/><text x="110" y="38" fill="#fff">1</text>
          <circle cx="224" cy="33" r="15" fill="var(--sky)"/><text x="224" y="38" fill="#fff">2</text>
        </g>
        <g fill="#fff" stroke="#e4ebf3">
          <circle cx="338" cy="33" r="14"/><circle cx="452" cy="33" r="14"/><circle cx="566" cy="33" r="14"/><circle cx="680" cy="33" r="14"/><circle cx="795" cy="33" r="14"/><circle cx="909" cy="33" r="14"/><circle cx="1023" cy="33" r="14"/>
        </g>
        <g fill="#8a929b">
          <text x="338" y="38">3</text><text x="452" y="38">4</text><text x="566" y="38">5</text><text x="680" y="38">6</text><text x="795" y="38">7</text><text x="909" y="38">8</text><text x="1023" y="38">9</text>
        </g>
      </svg>
    </nav>

    <h2 class="form-title">Customer Information:</h2>

    <div class="field" style="left:110px;top:270px;width:430px"><label>Who passed credit?</label><div class="box"></div></div>
    <div class="field" style="left:600px;top:270px;width:440px"><label>Name as it appears on electric bill</label><div class="box"></div></div>

    <div class="field" style="left:110px;top:392px;width:430px"><label>Primary Owner (Full Name)</label><div class="box"></div></div>
    <div class="field" style="left:600px;top:392px;width:440px"><label>On Title?</label>
      <div class="box select"><span>-Select Option-</span>
        <span class="chevron"><svg width="20" height="12" viewBox="0 0 20 12"><path d="M2 2l8 8 8-8" fill="none" stroke="#fff" stroke-width="2"/></svg></span>
      </div>
    </div>

    <div class="field" style="left:110px;top:514px;width:286px"><label>Email</label><div class="box"></div></div>
    <div class="field" style="left:432px;top:514px;width:286px"><label>Home Phone</label><div class="box"></div></div>
    <div class="field" style="left:754px;top:514px;width:286px"><label>Cell Phone</label><div class="box"></div></div>

    <footer class="footer-band">
      <button class="btn btn-previous">Previous</button>
      <button class="btn btn-next">Next</button>
    </footer>
  </main>
</body>
</html>
```